Kiteloft Namecard

We have a regular but rotating group of Actors and Directors who meet weekly. I'd like to make a nametag (first and last names) for each of the participants which would fit on a regular business card. The first name would be over-sized to enable reading at a distance. The background & border should project fun and warmth. The Kiteloft is meant to be a place to play without judgement or negative vibes.

```html
<!DOCTYPE html>
<html lang="en">
<head>
<meta charset="utf-8">
<title>Kiteloft Namecard</title>
<link rel="stylesheet" href="https://fonts.googleapis.com/css2?family=Dancing+Script:wght@400&family=Quicksand:wght@400&display=swap">
<style>
  :root {
    --sky-deep: #1f2f6e;
    --sky-blue: #4d5f9c;
    --dusk-violet: #7a6a8e;
    --plum: #8a5a78;
    --rose: #b88a92;
    --peach: #d9b8a8;
    --glow: #f1d6a4;
    --halo: rgba(255, 255, 255, 0.26);
    --ink: #ffffff;
  }
  html, body {
    margin: 0;
    padding: 0;
    overflow: hidden;
    background: #e9e6ea;
  }
  .namecard {
    position: relative;
    width: 1200px;
    height: 686px;
    overflow: hidden;
    background:
      radial-gradient(ellipse 420px 260px at 300px 690px, var(--glow) 0%, rgba(241,214,164,0) 70%),
      radial-gradient(ellipse 520px 320px at 780px 520px, var(--peach) 0%, rgba(217,184,168,0) 75%),
      radial-gradient(ellipse 360px 420px at 1130px 340px, var(--plum) 0%, rgba(138,90,120,0) 75%),
      radial-gradient(ellipse 460px 320px at 1000px 620px, var(--rose) 0%, rgba(184,138,146,0) 75%),
      radial-gradient(ellipse 520px 360px at 120px 440px, var(--dusk-violet) 0%, rgba(122,106,142,0) 75%),
      radial-gradient(ellipse 700px 360px at 200px 40px, var(--sky-deep) 0%, rgba(31,47,110,0) 80%),
      radial-gradient(ellipse 600px 300px at 1100px 20px, var(--sky-blue) 0%, rgba(77,95,156,0) 80%),
      linear-gradient(180deg, var(--sky-blue) 0%, var(--dusk-violet) 55%, var(--rose) 100%);
  }
  .halo {
    position: absolute;
    left: 265px;
    top: 15px;
    width: 622px;
    height: 622px;
    border-radius: 50%;
    background: var(--halo);
  }
  .first-name {
    position: absolute;
    left: 340px;
    top: 118px;
    width: 472px;
    margin: 0;
    text-align: center;
    font-family: "Dancing Script", cursive;
    font-weight: 400;
    font-size: 250px;
    line-height: 1;
    color: var(--ink);
  }
  .last-name {
    position: absolute;
    left: 412px;
    top: 378px;
    width: 380px;
    margin: 0;
    text-align: center;
    font-family: "Quicksand", sans-serif;
    font-weight: 400;
    font-size: 34px;
    letter-spacing: 0.62em;
    line-height: 1;
    color: var(--ink);
    padding-left: 0.62em;
    box-sizing: border-box;
  }
</style>
</head>
<body>
  <main class="namecard">
    <div class="halo"></div>
    <h1 class="first-name">Nora</h1>
    <p class="last-name">BELLAMY</p>
  </main>
</body>
</html>
```